Modern Label for Loose Tea pouches on 4.5x6 Label

We need a new label for our teas that is very simple in design, but stylish and modern. This will be used to print labels for our loose tea pouches. The label will be at max 4.5x6 inches in size. There should be a place for the tea name, description, ingredients, and size that is changeable.
Preferably an AI file that allows me to setup variables to change the above items. There will also need to be our logo which is supplied, and our address on the label.
Address:
Brevo Leaf
846 Lower Maple Lane
Highland, NY 12617
Target Market(s)
Tea Lovers
Requirements
Must have
- Adobe Illustrator file with variables setup for replacement of tea name, description, ingredients, and size (weights 2oz, 4oz, 8oz, 1lb)

```html
<!DOCTYPE html>
<html lang="en">
<head>
<meta charset="utf-8">
<title>Good Morning – Brevo Leaf Tea Label</title>
<link rel="stylesheet" href="https://fonts.googleapis.com/css2?family=Fira+Sans:wght@300;400;600&display=swap">
<style>
  :root {
    --page: #efefef;
    --paper: #ffffff;
    --pink: #d6529a;
    --green: #b6d334;
    --ink: #231f20;
    --text: #2b2b2b;
    --white: #ffffff;
  }
  * { box-sizing: border-box; margin: 0; padding: 0; }
  html, body {
    width: 800px; height: 1200px; overflow: hidden;
    background: var(--page);
    font-family: "Fira Sans", Arial, sans-serif;
    color: var(--text);
  }
  .label {
    position: absolute; left: 40px; top: 120px;
    width: 720px; height: 960px;
    background: var(--paper);
    box-shadow: 0 2px 10px rgba(0,0,0,0.12);
  }
  .leaf-band {
    position: absolute; left: 30px; top: 20px;
    width: 213px; height: 751px;
    background: linear-gradient(180deg, var(--pink) 0%, #d95ea1 55%, var(--pink) 100%);
  }
  .brand {
    position: absolute; left: 243px; top: 150px; width: 457px;
    display: flex; align-items: center; justify-content: center; gap: 14px;
  }
  .brand-dot {
    width: 22px; height: 22px; border-radius: 50%; background: var(--green);
  }
  .brand-name {
    font-weight: 600; font-size: 46px; letter-spacing: 2px;
    color: var(--pink);
  }
  .tea-name {
    position: absolute; left: 243px; top: 318px; width: 457px;
    text-align: center;
    font-weight: 300; font-size: 62px; line-height: 1.1; color: var(--ink);
  }
  .description {
    position: absolute; left: 280px; top: 536px; width: 412px;
  }
  .section-title {
    font-weight: 300; font-size: 36px; line-height: 1;
  }
  .description .section-title { color: var(--pink); margin-bottom: 28px; }
  .description p {
    font-size: 17px; line-height: 1.5; color: var(--text);
  }
  .net-weight {
    position: absolute; right: 20px; top: 730px;
    font-weight: 600; font-size: 16px; color: var(--pink);
  }
  .address {
    position: absolute; left: 30px; top: 771px;
    width: 213px; height: 169px;
    background: var(--green);
    padding: 22px 18px;
  }
  .address .section-title { color: var(--ink); margin-bottom: 26px; }
  .address address {
    font-style: normal; font-weight: 600; font-size: 15px; line-height: 1.35; color: var(--ink);
  }
  .ingredients {
    position: absolute; left: 243px; top: 771px;
    width: 457px; height: 169px;
    background: var(--ink);
    padding: 22px 45px;
    color: var(--white);
  }
  .ingredients .section-title { margin-bottom: 26px; }
  .ingredients p { font-size: 16px; line-height: 1.4; }
</style>
</head>
<body>
  <main class="label">
    <div class="leaf-band" role="img" aria-label="White line drawing of a tea leaf sprig on a pink band"></div>

    <div class="brand">
      <span class="brand-dot"></span>
      <span class="brand-name">BREVO LEAF</span>
    </div>

    <h1 class="tea-name">Good<br>Morning</h1>

    <section class="description">
      <h2 class="section-title">Description:</h2>
      <p>Smooth and sublime, this organic rare white tea is enlivened with crisp apples and the flavor of sun-sweet tangerines. An alluring addition of fragrant rosemary adds to this savory garden cup. Refreshing iced!</p>
    </section>

    <p class="net-weight">Net Wt. 4 oz</p>

    <section class="address">
      <h2 class="section-title">Address:</h2>
      <address>Brevo Leaf<br>846 Lower Maple Lane<br>Highland, NY 12617</address>
    </section>

    <section class="ingredients">
      <h2 class="section-title">Ingredients:</h2>
      <p>Senna Leaf, Buckthorn Bark, Fennel Seed,<br>Chamomile, Peppermint, Cinnamon Bark</p>
    </section>
  </main>
</body>
</html>
```